Bravados- Tattoos/Piercings/Motorcycle/Biker Appearl Shop

Bravados' buisness cards can be creative, playful and eye catching. Incorporate leather or diamond plate. We are an all female business. Biker theme, Tattoo Photos, Piercing Photos, Diamond plate, Leather and Girls!

This project needs to be an appointment card as well for the tattoo artists and piercers. We need a section that says APPT With: _______ , DATE, TIME, and then a QUOTE and DEPOSIT section for the artists. I attached the logo so you could incorportate that and have complete creative freedom. It's a biker store, we sell biker appearl and accessories, with a tattoo and piercing shop connected. Girls, Leather, Tattoos and Piercings. Have fun with it!

I've Updated project details for better description of what im looking for. Thanks!

Target Market(s)

Male and Female Ages 15-90. Interests in custom tattoos and quality piercings, bikers, motorcycle accessories like helmets, gloves, masks, leather, boots. Jewlery and clothes.

Industry/Entity Type

Business

Contact Information for Business Card

The business is called Bravados, address, phone number and website. (2837 Wexley Ave. Muskegon, MI. 49517 (231)472-9035 www.inkridgeparlor.com)

Font styles to use
Serif
Sans Serif
Decorative
Script

Requirements
Must have
• Appointment with______
• Date_____ or MON TUES WED THUR etc... check mark boxes
• Time_____
• Quote______
• Deposit_______
• (231) 472-9035
• 2837 Wexley Ave
• Muskegon, MI 49517
• a facebook logo
Nice to have
• Owner Rick Hollowell
Should not have
• Tribal dragons or anything Tribal.That's cheesy! No Butterflies, No stars. No boys,

```html
<!DOCTYPE html>
<html lang="en">
<head>
<meta charset="utf-8">
<title>Bravados – Appointment & Business Card</title>
<link href="https://fonts.googleapis.com/css2?family=Abel&family=Architects+Daughter&display=swap" rel="stylesheet">
<style>
  :root {
    --page-bg: #e9e6e1;
    --card-white: #ffffff;
    --card-black: #141414;
    --card-black-edge: #2a2a2a;
    --ink-dark: #2b2b2b;
    --rule-line: #3a3a3a;
    --blush: #efdcdc;
    --blush-mid: rgba(226, 196, 198, 0.42);
    --blush-faint: rgba(201, 174, 176, 0.08);
    --contact-grey: #cfcaca;
  }
  html, body {
    margin: 0;
    padding: 0;
    width: 1200px;
    height: 900px;
    overflow: hidden;
    background: var(--page-bg);
  }
  .canvas {
    position: relative;
    width: 1200px;
    height: 900px;
  }
  .card {
    position: absolute;
    left: 250px;
    width: 700px;
    height: 400px;
    border-radius: 4px;
    box-shadow: 0 6px 18px rgba(0,0,0,0.18);
    overflow: hidden;
  }

  /* Appointment side */
  .card--appointment {
    top: 40px;
    background: var(--card-white);
  }
  .appointment-fields {
    list-style: none;
    margin: 0;
    padding: 0;
    position: absolute;
    left: 60px;
    top: 95px;
    width: 590px;
  }
  .appointment-field {
    display: flex;
    align-items: flex-end;
    height: 46px;
    font-family: "Architects Daughter", cursive;
    font-size: 26px;
    color: var(--ink-dark);
  }
  .appointment-field__bullet {
    width: 12px;
    height: 12px;
    border-radius: 50%;
    background: var(--ink-dark);
    margin: 0 12px 10px 0;
    flex: none;
  }
  .appointment-field__label {
    white-space: nowrap;
    line-height: 1;
    padding-bottom: 4px;
  }
  .appointment-field__line {
    flex: 1;
    border-bottom: 1.5px solid var(--rule-line);
    margin: 0 0 8px 18px;
  }

  /* Business side */
  .card--business {
    top: 460px;
    background: radial-gradient(ellipse at 60% 35%, var(--card-black-edge), var(--card-black) 70%);
  }
  .flourish {
    position: absolute;
    border-radius: 3px;
  }
  .flourish--top-left {
    left: 22px; top: 28px; width: 26px; height: 96px;
    background: linear-gradient(180deg, var(--blush-mid), var(--blush-faint));
  }
  .flourish--top-left-arm {
    left: 22px; top: 28px; width: 120px; height: 18px;
    background: linear-gradient(90deg, var(--blush-mid), var(--blush-faint));
  }
  .flourish--bottom-left {
    left: 40px; top: 250px; width: 26px; height: 128px;
    background: linear-gradient(0deg, var(--blush-mid), var(--blush-faint));
  }
  .flourish--bottom-left-arm {
    left: 40px; top: 360px; width: 170px; height: 18px;
    background: linear-gradient(90deg, var(--blush-mid), var(--blush-faint));
  }
  .flourish--top-right {
    right: 22px; top: 18px; width: 200px; height: 18px;
    background: linear-gradient(270deg, var(--blush-mid), var(--blush-faint));
  }
  .flourish--top-right-arm {
    right: 22px; top: 18px; width: 26px; height: 70px;
    background: linear-gradient(180deg, var(--blush-mid), var(--blush-faint));
  }
  .flourish--right {
    right: 22px; top: 170px; width: 26px; height: 150px;
    background: linear-gradient(0deg, var(--blush-mid), var(--blush-faint));
  }
  .flourish--right-arm {
    right: 22px; top: 302px; width: 150px; height: 18px;
    background: linear-gradient(270deg, var(--blush-mid), var(--blush-faint));
  }

  .brand {
    position: absolute;
    left: 0;
    right: 0;
    top: 72px;
    text-align: center;
    font-family: "Abel", sans-serif;
    font-size: 108px;
    line-height: 1;
    letter-spacing: 4px;
    color: var(--blush);
    margin: 0;
  }
  .divider {
    position: absolute;
    left: 170px;
    top: 212px;
    width: 400px;
    height: 24px;
  }
  .contact {
    position: absolute;
    left: 0;
    right: 0;
    top: 254px;
    text-align: center;
    font-family: "Abel", sans-serif;
    font-style: normal;
    color: var(--contact-grey);
    font-size: 22px;
    line-height: 1.4;
    letter-spacing: 1px;
  }
  .contact__phone { font-size: 26px; }
</style>
</head>
<body>
<main class="canvas">

  <section class="card card--appointment" aria-label="Appointment card">
    <ul class="appointment-fields">
      <li class="appointment-field"><span class="appointment-field__bullet"></span><span class="appointment-field__label">Appointment with</span><span class="appointment-field__line"></span></li>
      <li class="appointment-field"><span class="appointment-field__bullet"></span><span class="appointment-field__label">Date</span><span class="appointment-field__line"></span></li>
      <li class="appointment-field"><span class="appointment-field__bullet"></span><span class="appointment-field__label">Time</span><span class="appointment-field__line"></span></li>
      <li class="appointment-field"><span class="appointment-field__bullet"></span><span class="appointment-field__label">Quote</span><span class="appointment-field__line"></span></li>
      <li class="appointment-field"><span class="appointment-field__bullet"></span><span class="appointment-field__label">Deposit</span><span class="appointment-field__line"></span></li>
    </ul>
  </section>

  <section class="card card--business" aria-label="Business card">
    <div class="flourish flourish--top-left" role="img" aria-label="Pink floral corner flourish"></div>
    <div class="flourish flourish--top-left-arm" aria-hidden="true"></div>
    <div class="flourish flourish--bottom-left" role="img" aria-label="Pink floral corner flourish"></div>
    <div class="flourish flourish--bottom-left-arm" aria-hidden="true"></div>
    <div class="flourish flourish--top-right" role="img" aria-label="Pink floral corner flourish"></div>
    <div class="flourish flourish--top-right-arm" aria-hidden="true"></div>
    <div class="flourish flourish--right" role="img" aria-label="Pink floral side flourish"></div>
    <div class="flourish flourish--right-arm" aria-hidden="true"></div>

    <h1 class="brand">Bravados</h1>

    <svg class="divider" viewBox="0 0 400 24" aria-hidden="true">
      <line x1="0" y1="20" x2="170" y2="13" stroke="#efdcdc" stroke-width="2" stroke-dasharray="14 6"/>
      <line x1="230" y1="11" x2="400" y2="4" stroke="#efdcdc" stroke-width="2" stroke-dasharray="14 6"/>
      <circle cx="200" cy="12" r="5" fill="#efdcdc"/>
    </svg>

    <address class="contact">
      <div class="contact__address">2837 Wexley Ave. Muskegon, MI 49517</div>
      <div class="contact__phone">(231) 472-9035</div>
      <div class="contact__web">www.inkridgeparlor.com</div>
    </address>
  </section>

</main>
</body>
</html>
```